Letterhead design of MERIDOR POWER KEEPER INC.

we are a energy saving company doing the solar screen, radian barrier, attic insulation, double panel windows. Basically i need the design of the letterhead including my company name, business address, phone numbers, fax number and email address. Main thing i need it look like a huge company and look like very high class. thanks !!

Reason: Please send me more new design about my company! Thanks so much!!

Industry/Entity Type

Business

```html
<!DOCTYPE html>
<html lang="en">
<head>
<meta charset="utf-8">
<title>Meridor Power Keeper Inc. — Letterhead</title>
<link rel="stylesheet" href="https://fonts.googleapis.com/css2?family=Arimo:wght@400;700&display=swap">
<style>
  :root {
    --paper: #ffffff;
    --ink: #111111;
    --brand-grey: #58595b;
    --brand-green: #7dc242;
    --brand-orange: #f26522;
    --rule: #6d6e71;
  }
  * { margin: 0; padding: 0; box-sizing: border-box; }
  html, body {
    width: 900px;
    height: 1200px;
    overflow: hidden;
    background: var(--paper);
  }
  .letterhead {
    position: relative;
    width: 900px;
    height: 1200px;
    background: var(--paper);
    font-family: "Arimo", Arial, sans-serif;
    color: var(--ink);
  }
  .brand {
    position: absolute;
    left: 54px;
    top: 60px;
    display: flex;
    align-items: center;
    gap: 22px;
  }
  .brand__dot {
    width: 96px;
    height: 96px;
    border-radius: 50%;
    background: var(--brand-orange);
  }
  .brand__name {
    color: var(--brand-grey);
    font-weight: 700;
    line-height: 1;
  }
  .brand__name-main {
    display: block;
    font-size: 54px;
    letter-spacing: -1px;
  }
  .brand__name-sub {
    display: block;
    font-size: 28px;
    margin-top: 4px;
  }
  .contact {
    position: absolute;
    left: 578px;
    top: 68px;
    width: 280px;
    padding-top: 8px;
    text-align: right;
    font-size: 15px;
    line-height: 1.3;
  }
  .contact::before {
    content: "";
    position: absolute;
    left: 0;
    top: 0;
    width: 1px;
    height: 206px;
    background: var(--rule);
  }
  .contact__company { font-weight: 700; }
  .contact__block + .contact__block { margin-top: 18px; }
  .watermark {
    position: absolute;
    left: 400px;
    top: 660px;
    width: 420px;
    height: 420px;
    border-radius: 50%;
    background: radial-gradient(circle at 40% 40%, rgba(242,101,34,0.10), rgba(125,194,66,0.08) 60%, rgba(125,194,66,0) 75%);
  }
  .footer-band {
    position: absolute;
    left: 0;
    bottom: 56px;
    width: 100%;
    height: 22px;
    display: flex;
  }
  .footer-band__green { flex: 0 0 734px; background: var(--brand-green); }
  .footer-band__orange { flex: 1; background: var(--brand-orange); }
</style>
</head>
<body>
  <main class="letterhead">
    <header class="brand">
      <span class="brand__dot"></span>
      <span class="brand__name">
        <span class="brand__name-main">MERIDOR</span>
        <span class="brand__name-sub">Power Keeper</span>
      </span>
    </header>

    <address class="contact" style="font-style: normal;">
      <div class="contact__block">
        <div class="contact__company">Meridor Power Keeper Inc.</div>
        <div>4827 Corvell Rd Suite</div>
        <div>#210 Brenfield, TEXAS 75550</div>
      </div>
      <div class="contact__block">
        <div>Phone 555-014-2873</div>
        <div>Fax&nbsp; 555-019-4416</div>
      </div>
      <div class="contact__block">
        <div>Email hello@meridorpowerkeeper.com</div>
      </div>
    </address>

    <div class="watermark" aria-hidden="true"></div>

    <div class="footer-band" aria-hidden="true">
      <span class="footer-band__green"></span>
      <span class="footer-band__orange"></span>
    </div>
  </main>
</body>
</html>
```